Medical Marijuana Potato Chip Bags Need Graphic Design

We are looking for a bag design for our new brand of medical marijuana potato chips. The design should be simple, the less colors used the better. We are looking for a classic kind of potato chip design somewhere between that of the bag design of Harrow Lane Potato Chips, Brinna's Pita Chips and Fell Ridge Potato Chips.

The main logo is "Toasty Grove Munchies" with "Potato Chips" written underneath it. The original idea was to have a simple sketch of a POTATO SMOKING A JOINT underneath the font, open to other ideas but that would be ideal. In terms of texture and color, we are very open but if you're lost use a burlap sack as influence

This is for the front and back so the design should be able to wrap around. Details such as nutrition info will be added later.
The dimensions are 10"x8" (that includes front and back) or two 5"x8" pictures (one for front, one for back).
Remember that it must appeal to the variety of patients using medical marijuana, from young adults with minor ailments to senior citizens with terminal diseases.

We've decided to make our project non-refundable so the best idea will be rewarded!

Reason: We are just waiting on a few more designs from designers who requested more time. Great job on all the designs so far!

```html
<!DOCTYPE html>
<html lang="en">
<head>
<meta charset="utf-8">
<title>Toasty Grove Munchies – Potato Chips Bag Front and Back</title>
<link href="https://fonts.googleapis.com/css2?family=Arvo:wght@400;700&family=Cinzel:wght@700&display=swap" rel="stylesheet">
<style>
  :root {
    --canvas: #ffffff;
    --burlap: #bdb09a;
    --burlap-stripe: #ad9f87;
    --burlap-light: #c9bda8;
    --cream: #f2ece0;
    --stitch: #6e4f3a;
    --leaf-light: #8fd07f;
    --leaf-mid: #4f9c47;
    --leaf-deep: #2f7a33;
    --ribbon-top: #93d483;
    --ribbon-bottom: #66b658;
    --ribbon-shade: #3d7a35;
    --emblem: #0e3b1f;
    --emblem-mid: #2c5e3a;
    --emblem-ring: #9aa39c;
    --label-white: #ffffff;
    --purple: #7b1d8e;
    --gold-a: #f6c978;
    --gold-b: #e9a545;
    --ink-grey: #555555;
  }
  * { box-sizing: border-box; margin: 0; padding: 0; }
  html, body { width: 1000px; height: 1200px; overflow: hidden; background: var(--canvas); }
  .canvas { position: relative; width: 1000px; height: 1200px; background: var(--canvas); }

  .panel {
    position: absolute; top: 243px; width: 440px; height: 714px;
    background-color: var(--burlap);
    background-image: repeating-linear-gradient(90deg,
      var(--burlap-light) 0 3px,
      var(--burlap) 3px 7px,
      var(--burlap-stripe) 7px 9px,
      var(--burlap) 9px 12px);
    box-shadow: 0 3px 8px rgba(0,0,0,0.3);
    overflow: hidden;
  }
  .panel--back { left: 40px; }
  .panel--front { left: 520px; }

  .band {
    position: absolute; left: 0; right: 0; height: 68px; background: var(--cream);
  }
  .band--top { top: 18px; }
  .band--bottom { bottom: 12px; }
  .band__stitch {
    position: absolute; left: 14px; right: 14px; height: 0;
    border-top: 3px dashed var(--stitch); opacity: 0.85;
  }
  .band--top .band__stitch { top: 10px; }
  .band--bottom .band__stitch { bottom: 8px; }
  .band__leaves {
    position: absolute; left: 18px; right: 18px; height: 20px;
    background: linear-gradient(90deg, var(--leaf-light), var(--leaf-mid) 50%, var(--leaf-light));
    border-radius: 10px; opacity: 0.8;
  }
  .band--top .band__leaves { top: 31px; }
  .band--bottom .band__leaves { top: 17px; }

  .label {
    position: absolute; left: 22px; right: 22px; top: 92px; height: 540px;
    background: var(--label-white);
    border-radius: 50% 50% 6px 6px / 14% 14% 6px 6px;
    box-shadow: inset 0 0 0 1px rgba(0,0,0,0.05);
  }

  .crown {
    position: absolute; left: 50%; top: 104px; width: 300px; height: 78px;
    transform: translateX(-50%);
    background: linear-gradient(180deg, var(--leaf-light), var(--leaf-mid) 55%, var(--emblem));
    border-radius: 50% 50% 0 0 / 90% 90% 0 0;
  }

  .ribbon {
    position: absolute; left: 0; right: 0; top: 178px; height: 82px;
    background: linear-gradient(180deg, var(--ribbon-top), var(--ribbon-bottom));
    text-align: center; color: var(--label-white);
    font-family: "Arvo", Georgia, serif;
  }
  .ribbon__name {
    display: block; font-size: 34px; font-weight: 700; line-height: 1;
    padding-top: 10px; letter-spacing: 0.5px;
  }
  .ribbon__sub {
    display: block; font-size: 28px; font-weight: 400; line-height: 1;
    margin-top: 6px; letter-spacing: 1px;
  }

  .badge-new {
    position: absolute; left: 4px; top: 96px; width: 80px; height: 36px;
    background: linear-gradient(90deg, var(--gold-a), var(--gold-b));
    color: var(--purple);
    font-family: "Arvo", Georgia, serif; font-weight: 700; font-size: 24px;
    line-height: 36px; text-align: center;
  }

  .emblem {
    position: absolute; left: 50%; top: 333px; width: 192px; height: 192px;
    transform: translateX(-50%);
  }

  .product {
    position: absolute; left: 44px; right: 44px; top: 572px;
    display: flex; align-items: center; gap: 12px;
    color: var(--purple);
    font-family: "Cinzel", "Times New Roman", serif; font-weight: 700; font-size: 22px;
    white-space: nowrap;
  }
  .product::before, .product::after {
    content: ""; flex: 1; height: 2px; background: var(--purple);
  }

  .net-weight {
    position: absolute; right: 30px; top: 610px;
    font-family: "Times New Roman", serif; font-size: 13px; color: var(--ink-grey);
  }
</style>
</head>
<body>
<main class="canvas">

  <section class="panel panel--back" aria-label="Bag back">
    <div class="band band--top">
      <div class="band__stitch"></div>
      <div class="band__leaves" role="img" aria-label="Row of small green leaf motifs"></div>
    </div>
    <div class="band band--bottom">
      <div class="band__leaves" role="img" aria-label="Row of small green leaf motifs"></div>
      <div class="band__stitch"></div>
    </div>
  </section>

  <section class="panel panel--front" aria-label="Bag front">
    <div class="band band--top">
      <div class="band__stitch"></div>
      <div class="band__leaves" role="img" aria-label="Row of small green leaf motifs"></div>
    </div>

    <div class="label"></div>

    <div class="crown" role="img" aria-label="Cluster of green leaves rising above the name"></div>

    <div class="badge-new">NEW</div>

    <h1 class="ribbon">
      <span class="ribbon__name">TOASTY GROVE</span>
      <span class="ribbon__sub">MUNCHIES</span>
    </h1>

    <svg class="emblem" viewBox="0 0 192 192" role="img" aria-label="Round dark green seal with a large pale leaf illustration">
      <defs>
        <radialGradient id="seal-fill" cx="50%" cy="50%" r="50%">
          <stop offset="0%" stop-color="var(--emblem-mid)"/>
          <stop offset="100%" stop-color="var(--emblem)"/>
        </radialGradient>
      </defs>
      <circle cx="96" cy="96" r="92" fill="none" stroke="var(--emblem-ring)" stroke-width="5" stroke-dasharray="3 3"/>
      <circle cx="96" cy="96" r="87" fill="none" stroke="var(--emblem-ring)" stroke-width="1.5"/>
      <circle cx="96" cy="96" r="83" fill="url(#seal-fill)"/>
    </svg>

    <p class="product">POTATO CHIPS</p>
    <p class="net-weight">32.5g e</p>

    <div class="band band--bottom">
      <div class="band__leaves" role="img" aria-label="Row of small green leaf motifs"></div>
      <div class="band__stitch"></div>
    </div>
  </section>

</main>
</body>
</html>
```